Business card design needed

Willowby Studio

I would like a design for a small business specializing in earrings made from Tasmanian timber combined with coloured beads. I see the brand as a modern take on wooden earrings, fun and beautiful with the wood being laser cut Tasmanian timber combined with a coloured sometimes metallic bead.

I see the logo design as a little cute, perhaps a ladybug on a leaf and would like a combination of green and white. I have seen a quirky take on the traditional red ladybug done in pink with black spots on a green leaf that I like but I'm very open to ideas and suggestions.

Target Market(s)

Women primarily aged 20-50

Industry/Entity Type

Small Business

Contact Information for Business Card

Willowby Studio
Tasmanian Timber & Beaded Design Earrings

www.pagebook.example/willowby
www.craftnook.example/willowby

Logo Text

Willowby Studio

Requirements
Must have
• Must have some white on the business card. The cards are being matched with Tasmanian Timber earrings so whites and greens with a splash of colour is okay, but nothing to crazy or bright.

```html
<!DOCTYPE html>
<html lang="en">
<head>
<meta charset="utf-8">
<title>Willowby Studio – Business Cards</title>
<link href="https://fonts.googleapis.com/css2?family=Italianno&family=Jost:wght@400;500&display=swap" rel="stylesheet">
<style>
  :root {
    --backdrop: #e6e5e1;
    --card-white: #f3f4f5;
    --card-shadow: rgba(40, 35, 30, 0.22);
    --ink: #1c1c1c;
    --ink-soft: #2e2e2e;
    --watermark-grey: #c9cbcd;
    --leaf-light: #8cc63f;
    --leaf-mid: #4fa72e;
    --leaf-deep: #2f7d1f;
    --rule: #4a4a4a;
  }
  * { margin: 0; padding: 0; box-sizing: border-box; }
  html, body {
    width: 1200px; height: 880px; overflow: hidden;
    background: var(--backdrop);
  }
  .canvas { position: relative; width: 1200px; height: 880px; }

  .card {
    position: absolute;
    background: var(--card-white);
    box-shadow: 0 10px 24px var(--card-shadow), 0 2px 4px rgba(0,0,0,0.12);
    overflow: hidden;
  }

  /* Contact side (landscape) */
  .card--contact { left: 90px; top: 300px; width: 580px; height: 330px; }
  .contact-list {
    position: absolute; left: 70px; top: 52px; width: 360px;
    list-style: none; text-align: center;
    font-family: 'Jost', sans-serif; font-weight: 400;
    font-size: 15px; letter-spacing: 2.2px; text-transform: uppercase;
    color: var(--ink-soft); line-height: 27px;
  }
  .contact-list li { white-space: nowrap; }
  .watermark-name {
    position: absolute; left: 26px; bottom: 26px;
    font-family: 'Italianno', cursive; font-size: 64px;
    color: var(--watermark-grey); white-space: nowrap; line-height: 1;
  }
  .contact-leaf { position: absolute; right: 0; bottom: 0; width: 240px; height: 250px; }

  /* Brand side (portrait) */
  .card--brand { left: 770px; top: 150px; width: 330px; height: 580px; }
  .brand-leaves { position: absolute; left: 65px; top: 70px; width: 200px; height: 210px; }
  .brand-name {
    position: absolute; left: 0; right: 0; top: 312px; text-align: center;
    font-family: 'Italianno', cursive; font-weight: 400; font-size: 58px; color: var(--ink);
    line-height: 1; white-space: nowrap;
  }
  .brand-rule {
    position: absolute; left: 40px; right: 40px; top: 400px;
    height: 1px; background: var(--rule);
  }
  .brand-tagline {
    position: absolute; left: 0; right: 0; top: 418px; text-align: center;
    font-family: 'Jost', sans-serif; font-weight: 400;
    font-size: 12.5px; letter-spacing: 2px; text-transform: uppercase;
    color: var(--ink-soft); line-height: 22px;
  }
</style>
</head>
<body>
<main class="canvas">

  <section class="card card--contact" aria-label="Card back with contact details">
    <ul class="contact-list">
      <li>hello@willowby.example</li>
      <li>www.pagebook.example/willowby</li>
      <li>www.craftnook.example/willowby</li>
    </ul>
    <p class="watermark-name">Willowby Studio</p>
    <svg class="contact-leaf" viewBox="0 0 240 250" role="img"
         aria-label="Illustration of a large green leaf with a pink ladybug resting on it">
      <defs>
        <linearGradient id="contactLeafFill" x1="0" y1="1" x2="1" y2="0">
          <stop offset="0" stop-color="var(--leaf-deep)"/>
          <stop offset="0.55" stop-color="var(--leaf-mid)"/>
          <stop offset="1" stop-color="var(--leaf-light)"/>
        </linearGradient>
      </defs>
      <path d="M30 250 C 40 150, 120 40, 240 0 L 240 250 Z" fill="url(#contactLeafFill)"/>
    </svg>
  </section>

  <section class="card card--brand" aria-label="Card front with brand name">
    <svg class="brand-leaves" viewBox="0 0 200 210" role="img"
         aria-label="Illustration of three green leaves with a small pink ladybug">
      <defs>
        <linearGradient id="brandLeafFill" x1="0" y1="1" x2="1" y2="0">
          <stop offset="0" stop-color="var(--leaf-deep)"/>
          <stop offset="0.5" stop-color="var(--leaf-mid)"/>
          <stop offset="1" stop-color="var(--leaf-light)"/>
        </linearGradient>
      </defs>
      <ellipse cx="100" cy="105" rx="96" ry="100" fill="url(#brandLeafFill)"/>
    </svg>
    <h1 class="brand-name">Willowby Studio</h1>
    <div class="brand-rule"></div>
    <p class="brand-tagline">Timber &amp; Bead Earrings<br>Handmade in Tasmania</p>
  </section>

</main>
</body>
</html>
```